Sports Nutrition line needs new label look/feel

We need a new label design for "Velmo",our Sports Nutrition line of vitamins, nutraceuticals, protein powders, and performance endurance products. We would like to see two separate designs, one blue and one red, as these are the two colors we are torn between. The labels should have the look/feel of a sports or fitness label, bold coloring, lettering, and even some use of holographic foiling.
Brands we would be similar to those found on ploverstack.com and quillmarshgoods.com. Brands we like in particular are KTR and Temlux.

Target Market(s)

Fitness enthusiasts,athletes, health nuts..

Industry/Entity Type

Nutrition

Font styles to use
Sans Serif
Decorative
Script

Colors
ec1f27
0692cd
0355a3
3276b5
f04a50

Requirements
Must have
• -Fitness look/feel
• -bold colors (preferably red and blue)
• -use of icons (eye health, brain, health, etc.)
• -"Fit" in "VelMO" must stand out
• -use tagline "Building Healthy Bodies"
Nice to have
• -holographic foiling elements
• -try to incorporate a molecular element (like those shown in the example labels)
Should not have
• -Light, calming colors
• -difficult to read fonts

```html
<!DOCTYPE html>
<html lang="en">
<head>
<meta charset="utf-8">
<title>Velmo Label</title>
<link rel="stylesheet" href="https://fonts.googleapis.com/css2?family=Raleway:wght@700;800&family=Questrial&display=swap">
<style>
  :root {
    --page-bg: #f2f2f2;
    --label-red: #ec1f27;
    --label-red-deep: #d81920;
    --label-red-soft: #f04a50;
    --ink: #1a1a1a;
    --ink-soft: #2b2b2b;
    --white: #ffffff;
  }
  html, body {
    margin: 0;
    padding: 0;
    width: 1200px;
    height: 960px;
    overflow: hidden;
    background: var(--page-bg);
  }
  .canvas {
    position: relative;
    width: 1200px;
    height: 960px;
  }
  .label {
    position: absolute;
    left: 100px;
    top: 126px;
    width: 1000px;
    height: 706px;
    background: radial-gradient(ellipse at 50% 40%, var(--label-red) 0%, var(--label-red-deep) 100%);
    overflow: hidden;
    font-family: "Raleway", sans-serif;
  }
  .label__pattern {
    position: absolute;
    inset: 0;
    background: linear-gradient(160deg, rgba(255,255,255,0.06) 0%, rgba(255,255,255,0) 50%, rgba(0,0,0,0.04) 100%);
  }
  .brand-name {
    position: absolute;
    left: 0;
    right: 0;
    top: 200px;
    margin: 0;
    text-align: center;
    font-family: "Raleway", sans-serif;
    font-weight: 800;
    font-size: 132px;
    line-height: 150px;
    letter-spacing: 2px;
    color: var(--ink);
  }
  .tagline {
    position: absolute;
    left: 55px;
    right: 65px;
    top: 350px;
    height: 62px;
    border-top: 4px solid var(--ink);
    border-bottom: 4px solid var(--ink);
    margin: 0;
    text-align: center;
    font-family: "Raleway", sans-serif;
    font-weight: 800;
    font-size: 57px;
    line-height: 62px;
    color: var(--white);
    letter-spacing: 0.5px;
    white-space: nowrap;
  }
  .subtitle {
    position: absolute;
    left: 0;
    right: 0;
    top: 428px;
    margin: 0;
    text-align: center;
    font-family: "Questrial", sans-serif;
    font-size: 44px;
    line-height: 52px;
    color: var(--ink-soft);
    letter-spacing: 0.5px;
  }
  .benefit-icons {
    position: absolute;
    left: 0;
    right: 0;
    top: 528px;
    display: flex;
    justify-content: center;
    gap: 22px;
  }
  .benefit-icon {
    width: 82px;
    height: 82px;
  }
  .supply-bar {
    position: absolute;
    left: 253px;
    width: 488px;
    top: 650px;
    height: 56px;
    background: var(--ink);
    color: var(--white);
    font-family: "Questrial", sans-serif;
    font-size: 27px;
    line-height: 56px;
    text-align: center;
    white-space: nowrap;
  }
</style>
</head>
<body>
<div class="canvas">
  <section class="label">
    <div class="label__pattern" role="img" aria-label="Faint hexagonal molecular pattern across the red label"></div>

    <h1 class="brand-name">VELMO</h1>
    <h2 class="tagline">BUILDING HEALTHY BODIES</h2>
    <p class="subtitle">Antioxidant Formula to Boost Immunity</p>

    <div class="benefit-icons">
      <svg class="benefit-icon" viewBox="0 0 82 82" role="img" aria-label="Joint health icon">
        <circle cx="41" cy="41" r="38" fill="var(--label-red-deep)" stroke="var(--ink)" stroke-width="4"/>
        <circle cx="41" cy="41" r="26" fill="var(--label-red-soft)"/>
      </svg>
      <svg class="benefit-icon" viewBox="0 0 82 82" role="img" aria-label="Brain health icon">
        <circle cx="41" cy="41" r="38" fill="var(--label-red-deep)" stroke="var(--ink)" stroke-width="4"/>
        <circle cx="41" cy="41" r="26" fill="var(--label-red-soft)"/>
      </svg>
      <svg class="benefit-icon" viewBox="0 0 82 82" role="img" aria-label="Hair and skin health icon">
        <circle cx="41" cy="41" r="38" fill="var(--label-red-deep)" stroke="var(--ink)" stroke-width="4"/>
        <circle cx="41" cy="41" r="26" fill="var(--label-red-soft)"/>
      </svg>
      <svg class="benefit-icon" viewBox="0 0 82 82" role="img" aria-label="Eye health icon">
        <circle cx="41" cy="41" r="38" fill="var(--label-red-deep)" stroke="var(--ink)" stroke-width="4"/>
        <circle cx="41" cy="41" r="26" fill="var(--label-red-soft)"/>
      </svg>
      <svg class="benefit-icon" viewBox="0 0 82 82" role="img" aria-label="Blood cell health icon">
        <circle cx="41" cy="41" r="38" fill="var(--label-red-deep)" stroke="var(--ink)" stroke-width="4"/>
        <circle cx="41" cy="41" r="26" fill="var(--label-red-soft)"/>
      </svg>
    </div>

    <div class="supply-bar">90 Day Supply Dietary Supplement</div>
  </section>
</div>
</body>
</html>
```